Bright Nook Home Page (A Home Wellness e-commerce site & blog)

We need a dynamic home page created for a home wellness brand. Must be visually appealing and extremely mobile-friendly. Logos and a Navmap have been provided but that is just a guideline, PLEASE USE YOUR CREATIVITY.

Target Market(s)

1st target demo: females 24-48, 2nd target demo: all 24-48

Number of Pages Required

1 page

```html
<!DOCTYPE html>
<html lang="en">
<head>
<meta charset="UTF-8">
<title>Bright Nook – Home Wellness</title>
<link href="https://fonts.googleapis.com/css2?family=Lato:wght@400;700;900&display=swap" rel="stylesheet">
<style>
:root{
  --teal:#2bb3c2;
  --teal-dark:#1f97a5;
  --ink:#1c1c1c;
  --text:#444;
  --mist:#e2f4f5;
  --white:#fff;
  --night:#161616;
  --violet:#6a3fa0;
}
*{box-sizing:border-box;margin:0;padding:0}
html,body{width:1200px;height:3888px;overflow:hidden}
body{font-family:"Lato",sans-serif;color:var(--text);background:var(--white);position:relative}
.abs{position:absolute}
.btn{display:inline-flex;align-items:center;gap:8px;background:var(--teal);color:var(--white);font-weight:700;font-size:15px;letter-spacing:.5px;padding:10px 20px;border-radius:22px;text-transform:uppercase}
.btn .dot{width:16px;height:16px;border-radius:50%;background:var(--white);display:inline-block;position:relative}
.btn .dot:after{content:"";position:absolute;left:5px;top:4px;border-left:6px solid var(--teal);border-top:4px solid transparent;border-bottom:4px solid transparent}

/* top bar */
.topbar{top:0;left:0;width:1200px;height:32px;background:var(--teal);color:var(--white);font-size:13px;font-weight:700;display:flex;align-items:center;justify-content:center}
.topbar .socials{position:absolute;left:780px;top:9px;display:flex;gap:14px}
.topbar .socials i,.topbar .tools i{width:14px;height:14px;border-radius:50%;background:rgba(255,255,255,.85);display:block}
.topbar .tools{position:absolute;right:40px;top:9px;display:flex;gap:22px}

/* header */
.header{top:32px;left:0;width:1200px;height:108px;background:var(--white);display:flex;align-items:center;justify-content:space-between;padding:0 100px 0 120px}
.brand{display:flex;align-items:center;gap:10px;font-size:44px;font-weight:900;color:var(--ink);letter-spacing:-1px}
.brand .mark{width:20px;height:20px;background:var(--teal);border-radius:50%}
.nav{display:flex;gap:34px;font-size:16px;font-weight:700;color:var(--ink)}
.nav a{position:relative}
.nav a.active:after{content:"";position:absolute;left:0;right:0;bottom:-8px;height:3px;background:var(--teal)}

/* hero */
.hero{top:140px;left:0;width:1200px;height:600px;background:linear-gradient(180deg,#b9d2e6 0%,#dfe7ef 30%,#7a8ea3 55%,#8a6640 75%,#5b3e22 100%)}
.hero-copy{left:120px;top:200px;color:var(--white);width:560px}
.hero-copy h1{font-size:58px;font-weight:700;line-height:1.1;margin-bottom:14px;white-space:nowrap}
.hero-copy p{font-size:15px;line-height:1.6;margin-bottom:22px;opacity:.92;width:440px}
.hero-curve{top:640px;left:0}
.promo{top:700px;left:0;width:1200px;height:90px;background:var(--ink);color:var(--white);font-size:28px;font-weight:700;display:flex;align-items:center;justify-content:center}

/* about */
.about{top:790px;left:0;width:1200px;height:490px;background:var(--mist)}
.about-photo{left:120px;top:110px;width:420px;height:300px;border-radius:8px;background:linear-gradient(180deg,#7fb8bd 0%,#4f8f9a 50%,#3f7d6a 100%)}
.about-copy{left:632px;top:100px;width:440px}
.about-copy h2{font-size:40px;color:var(--ink);font-weight:700}
.squiggle{display:block;margin:6px 0 28px}
.about-copy p{font-size:15px;line-height:1.65;color:#333;margin-bottom:22px}

/* bliss grid */
.section-title{left:0;width:1200px;text-align:center;font-size:34px;font-weight:700;color:var(--ink)}
.tile{border-radius:6px;overflow:hidden}
.tile .cap{position:absolute;left:24px;bottom:24px;color:var(--white);font-size:20px;font-weight:700;line-height:1.3}

/* pay later */
.paylater{top:2460px;left:0;width:1200px;height:260px;background:var(--teal)}
.paylater h3{position:absolute;left:160px;top:88px;color:var(--white);font-size:38px;font-weight:900;line-height:1.05;text-transform:uppercase}
.paylater .partner{position:absolute;left:790px;top:100px;display:flex;align-items:center;gap:14px;color:var(--white);font-size:50px;font-weight:700}
.paylater .partner i{width:46px;height:46px;border-radius:50%;background:var(--white);display:block}

/* blog */
.blog-deco{left:0;top:3020px;width:150px;height:400px;background:radial-gradient(ellipse at 40% 50%,#9b82c8 0%,#b7a6d8 45%,rgba(255,255,255,0) 75%)}
.card{width:304px;height:432px;background:var(--white);border-radius:14px;box-shadow:0 6px 22px rgba(0,0,0,.18);overflow:hidden}
.card .ph{height:220px}
.card .body{padding:18px 18px}
.card h4{font-size:22px;color:var(--ink);margin-bottom:10px}
.card p{font-size:14px;line-height:1.5;margin-bottom:16px}
.card .btn{font-size:13px;padding:8px 16px}

/* footer */
.footer{top:3420px;left:0;width:1200px;height:468px;background:var(--night);color:#ddd}
.footer-brand{left:70px;top:200px;display:flex;align-items:center;gap:10px;font-size:40px;font-weight:900;color:var(--white);letter-spacing:-1px}
.footer-brand .mark{width:18px;height:18px;background:var(--teal);border-radius:50%}
.footer-social{left:78px;top:268px;display:flex;gap:16px}
.footer-social i{width:30px;height:30px;border-radius:50%;background:var(--teal);display:block}
.fcol h5{color:var(--teal);font-size:17px;font-weight:700;text-transform:uppercase;margin-bottom:18px}
.fcol li{list-style:none;font-size:15px;margin-bottom:12px;display:flex;gap:10px;align-items:center}
.fcol li:before{content:"";border-left:6px solid var(--teal);border-top:4px solid transparent;border-bottom:4px solid transparent}
.contact li:before{display:none}
.contact .ic{width:26px;height:26px;border-radius:50%;background:var(--teal);flex:none}
.newsletter form{display:flex;margin-top:4px}
.newsletter .field{width:210px;height:40px;background:var(--white);color:#999;font-size:14px;padding:11px 14px}
.newsletter .send{width:44px;height:40px;background:var(--teal)}
.footer-bottom{left:70px;top:438px;width:1060px;font-size:13px;display:flex;justify-content:space-between}
.footer-bottom b{color:var(--teal);font-weight:700}
.footer-rule{left:70px;top:420px;width:1060px;height:1px;background:#3a3a3a}
.chat{left:1040px;top:3730px;width:52px;height:52px;border-radius:50%;background:var(--teal);box-shadow:0 4px 12px rgba(0,0,0,.3)}
</style>
</head>
<body>

<div class="abs topbar">Free shipping on all orders $50 and over!
  <div class="socials"><i></i><i></i><i></i><i></i><i></i></div>
  <div class="tools"><i></i><i></i></div>
</div>

<header class="abs header">
  <div class="brand"><span class="mark"></span>Bright Nook</div>
  <nav class="nav"><a class="active">HOME</a><a>ABOUT US</a><a>FEATURED PRODUCT</a><a>BLOG</a><a>CONTACT US</a></nav>
</header>

<section class="abs hero" role="img" aria-label="Woman leaping joyfully above a mountain valley at sunrise"></section>
<div class="abs hero-copy">
  <h1>Your Bright Nook</h1>
  <p>Wellness starts at home. Discover gentle rituals, calming scents and simple tools that help you rest, recharge and feel good every day.</p>
  <span class="btn">Shop now <span class="dot"></span></span>
</div>
<svg class="abs hero-curve" width="1200" height="70" viewBox="0 0 1200 70" aria-hidden="true">
  <path d="M0 0 Q600 90 1200 0 L1200 70 L0 70Z" fill="#1c1c1c"/>
  <path d="M0 2 Q600 92 1200 2" fill="none" stroke="#2bb3c2" stroke-width="4"/>
</svg>
<div class="abs promo">50% off sale going on now! Because saving money also makes us happy</div>

<section class="abs about">
  <div class="abs about-photo" role="img" aria-label="Calm lake surrounded by forest"></div>
  <div class="abs about-copy">
    <h2>About Us</h2>
    <svg class="squiggle" width="70" height="12" viewBox="0 0 70 12" aria-hidden="true"><path d="M2 4 Q35 16 68 4" fill="none" stroke="#2bb3c2" stroke-width="4" stroke-linecap="round"/></svg>
    <p>They say that home is where the heart is. But home is also where your mind and body reside. At Bright Nook we believe that home should be your place of Zen. A respite from the crazy world outside those walls. It is where you recharge your soul so you can approach each day with the focus and energy necessary to conquer the world.</p>
    <span class="btn">Shop now <span class="dot"></span></span>
  </div>
</section>

<h2 class="abs section-title" style="top:1336px">The key to total bliss is nurturing the mind,body, and soul</h2>
<svg class="abs" style="left:565px;top:1388px" width="70" height="12" viewBox="0 0 70 12" aria-hidden="true"><path d="M2 4 Q35 16 68 4" fill="none" stroke="#2bb3c2" stroke-width="4" stroke-linecap="round"/></svg>

<div class="abs tile" style="left:112px;top:1460px;width:312px;height:300px;background:linear-gradient(135deg,#f0e2b8,#d9b86a 60%,#8c9a5a)" role="img" aria-label="Handmade soap bars with oil bottles and herbs"></div>
<div class="abs tile" style="left:440px;top:1460px;width:316px;height:300px;background:linear-gradient(135deg,#e6d4b8,#c7a77c 55%,#9a8a5e)" role="img" aria-label="Wooden bath brush, soap and lemon slices"></div>
<div class="abs tile" style="left:772px;top:1460px;width:316px;height:600px;background:linear-gradient(180deg,#e9ded6,#c9b1a2 55%,#7a6358)" role="img" aria-label="Woman relaxing with a facial mask at a spa"><span class="cap">Lorem ipsum dolor sit amet,<br>consectetur adipiscing elit</span></div>
<div class="abs tile" style="left:112px;top:1772px;width:312px;height:288px;background:linear-gradient(135deg,#f2e6c2,#e3bf5a 55%,#7e9a4c)" role="img" aria-label="Body cream jars with rosemary and oil"></div>
<div class="abs tile" style="left:440px;top:1772px;width:316px;height:288px;background:linear-gradient(135deg,#d9dcc4,#b7a3c9 45%,#c9a54a)" role="img" aria-label="Stacked colourful soaps with lavender and oil bottle"></div>
<div class="abs tile" style="left:112px;top:2072px;width:644px;height:300px;background:linear-gradient(90deg,#efe7e0,#d8c3b2 50%,#a88c78)" role="img" aria-label="Woman receiving a relaxing face massage"><span class="cap">Sed ut perspiciatis unde omnis iste natus error<br>sit voluptatem</span></div>
<div class="abs tile" style="left:772px;top:2072px;width:316px;height:300px;background:linear-gradient(135deg,#eef0e6,#d2b25a 50%,#6f8c4a)" role="img" aria-label="Glass bottles of herbal oil with fresh herbs"></div>

<section class="abs paylater">
  <h3>Don't sweat it you can<br>pay later</h3>
  <div class="partner"><i></i>Crumb Pay</div>
</section>

<h2 class="abs section-title" style="top:2756px">The Happy Blog</h2>
<svg class="abs" style="left:565px;top:2806px" width="70" height="12" viewBox="0 0 70 12" aria-hidden="true"><path d="M2 4 Q35 16 68 4" fill="none" stroke="#2bb3c2" stroke-width="4" stroke-linecap="round"/></svg>

<div class="abs blog-deco" role="img" aria-label="Sprigs of lavender"></div>

<article class="abs card" style="left:112px;top:2880px">
  <div class="ph" role="img" aria-label="Woman walking on a beach at sunset" style="background:linear-gradient(180deg,#e7b27a,#c98a4f 60%,#6b5a4a)"></div>
  <div class="body"><h4>Sed ut perspiciatis</h4><p>Lorem ipsum dolor sit amet, consectetur adipiscing elit, sed do eiusmod tempor incididunt ut labore et dolore magna aliqua. Quis ipsum suspendisse ultrices</p><span class="btn">Learn more <span class="dot"></span></span></div>
</article>
<article class="abs card" style="left:448px;top:2880px">
  <div class="ph" role="img" aria-label="Couple meditating together in a bright room" style="background:linear-gradient(180deg,#e9e4dc,#c9bfb1 60%,#8b8478)"></div>
  <div class="body"><h4>Sed ut perspiciatis</h4><p>Lorem ipsum dolor sit amet, consectetur adipiscing elit, sed do eiusmod tempor incididunt ut labore et dolore magna aliqua. Quis ipsum suspendisse ultrices</p><span class="btn">Learn more <span class="dot"></span></span></div>
</article>
<article class="abs card" style="left:788px;top:2880px">
  <div class="ph" role="img" aria-label="People walking in a snowy winter landscape" style="background:linear-gradient(180deg,#c7d6e4,#e8eef3 55%,#9aa6b2)"></div>
  <div class="body"><h4>Sed ut perspiciatis</h4><p>Lorem ipsum dolor sit amet, consectetur adipiscing elit, sed do eiusmod tempor incididunt ut labore et dolore magna aliqua. Quis ipsum suspendisse ultrices</p><span class="btn">Learn more <span class="dot"></span></span></div>
</article>

<footer class="abs footer">
  <svg class="abs" style="left:0;top:0" width="1200" height="60" viewBox="0 0 1200 60" aria-hidden="true">
    <path d="M0 0 L1200 0 L1200 40 Q600 -10 0 40Z" fill="#fff"/>
    <path d="M0 40 Q600 -10 1200 40" fill="none" stroke="#6a3fa0" stroke-width="5"/>
  </svg>
  <div class="abs footer-brand"><span class="mark"></span>Bright Nook</div>
  <div class="abs footer-social"><i></i><i></i><i></i><i></i></div>

  <div class="abs fcol" style="left:356px;top:120px">
    <h5>Quick links</h5>
    <ul><li>Home</li><li>About Us</li><li>Pages</li><li>Portfolio</li><li>Blog</li><li>Contact Us</li></ul>
  </div>
  <div class="abs fcol contact" style="left:560px;top:120px;width:220px">
    <h5>Contact us</h5>
    <ul>
      <li><span class="ic"></span>1234 Maple Lane, Suite 5, Fairview</li>
      <li><span class="ic"></span>123 456 7890</li>
      <li><span class="ic"></span>hello@brightnook.example</li>
    </ul>
  </div>
  <div class="abs fcol newsletter" style="left:852px;top:120px">
    <h5>Sign up for our newsletter</h5>
    <form><span class="field">Enter Email</span><span class="send"></span></form>
  </div>

  <div class="abs footer-rule"></div>
  <div class="abs footer-bottom"><span>© Copyright 2023 <b>BRIGHT NOOK</b> | All Rights Reserved</span><span>Privacy policy | Terms of Service</span></div>
</footer>

<div class="abs chat" aria-hidden="true"></div>

</body>
</html>
```